Discreet simple classy for adult entertainment

I would like a matte black business card with gold writing for my business. Keeping it simple. Having my following:

Lina frost
Events. Entertainment. Promotions
0477250618

or alternatively could have what i had on my previous card below but i think i prefer the above as again - discretion.

Maybe a nice gold line thru the card or some other very simple design . Or not open to ideas/ can be doublesided if any good ideas with that.

included pics of my old bus card. not sure weather i want a photo on it or not. if i do it wont be the same pic. i kinda wanted a card that was discreet so if it was in someones wallet they wouldn't neccessarily realise it was from a stripper.

Target Market(s)

men

Industry/Entity Type

Business

Contact Information for Business Card

Lina frost
0477250618

Requirements
Nice to have
• i don't know i am really open to anything. im giving my cards to guys so something they can have in their wallet that is discreet preferably.

```html
<!DOCTYPE html>
<html lang="en">
<head>
<meta charset="utf-8">
<title>Lina Frost – Business Card</title>
<link rel="stylesheet" href="https://fonts.googleapis.com/css2?family=Pinyon+Script&family=Roboto:wght@500;700&display=swap">
<style>
  :root {
    --backdrop: #e9e6e1;
    --card-black: #0b0b0b;
    --card-sheen: #222222;
    --gold-light: #f2e7b4;
    --gold: #d9c37e;
    --gold-deep: #a88c45;
    --ink-light: #f1f1f1;
  }
  * { margin: 0; padding: 0; box-sizing: border-box; }
  html, body {
    width: 1200px;
    height: 902px;
    overflow: hidden;
    background: var(--backdrop);
  }
  .stage {
    position: relative;
    width: 1200px;
    height: 902px;
  }
  .business-card {
    position: absolute;
    left: 100px;
    top: 165px;
    width: 1000px;
    height: 572px;
    background: linear-gradient(135deg, var(--card-sheen) 0%, var(--card-black) 45%, var(--card-black) 100%);
    border-radius: 6px;
    overflow: hidden;
    box-shadow: 0 18px 40px rgba(0,0,0,0.25);
  }
  .accent-lines {
    position: absolute;
    inset: 0;
    width: 100%;
    height: 100%;
  }
  .contact-line {
    position: absolute;
    left: 56px;
    top: 44px;
    display: flex;
    align-items: center;
    gap: 22px;
  }
  .phone-icon { width: 62px; height: 62px; }
  .phone-number {
    font-family: "Roboto", Arial, sans-serif;
    font-weight: 700;
    font-size: 58px;
    letter-spacing: 1px;
    color: var(--ink-light);
  }
  .ornament {
    position: absolute;
    left: 360px;
    top: 170px;
    width: 290px;
    height: 110px;
    background: radial-gradient(ellipse at center, rgba(217,195,126,0.55) 0%, rgba(168,140,69,0.25) 55%, rgba(11,11,11,0) 75%);
  }
  .card-name {
    position: absolute;
    left: 0;
    right: 0;
    top: 250px;
    text-align: center;
    font-family: "Pinyon Script", cursive;
    font-size: 150px;
    line-height: 1;
    color: var(--gold-light);
  }
  .services {
    position: absolute;
    left: 60px;
    right: 60px;
    bottom: 40px;
    display: flex;
    justify-content: space-between;
    list-style: none;
  }
  .service {
    display: flex;
    align-items: center;
    gap: 8px;
    font-family: "Roboto", Arial, sans-serif;
    font-weight: 500;
    font-size: 26px;
    color: var(--ink-light);
  }
  .tick { width: 16px; height: 16px; }
</style>
</head>
<body>
<main class="stage">
  <section class="business-card">
    <svg class="accent-lines" viewBox="0 0 1000 572" aria-hidden="true">
      <defs>
        <linearGradient id="gold-rule" x1="0" y1="1" x2="1" y2="0">
          <stop offset="0" stop-color="#a88c45" stop-opacity="0"/>
          <stop offset="0.3" stop-color="#d9c37e"/>
          <stop offset="0.7" stop-color="#f2e7b4"/>
          <stop offset="1" stop-color="#a88c45" stop-opacity="0"/>
        </linearGradient>
      </defs>
      <line x1="250" y1="470" x2="700" y2="110" stroke="url(#gold-rule)" stroke-width="2.5"/>
      <line x1="320" y1="500" x2="770" y2="140" stroke="url(#gold-rule)" stroke-width="2.5"/>
    </svg>

    <div class="contact-line">
      <svg class="phone-icon" viewBox="0 0 62 62" aria-hidden="true">
        <circle cx="31" cy="31" r="28" fill="none" stroke="var(--gold)" stroke-width="3"/>
        <path d="M22 17c2-1 4 0 5 2l2 5c1 2 0 3-1 4l-2 2c1 3 4 6 7 7l2-2c1-1 2-2 4-1l5 2c2 1 3 3 2 5l-1 2c-1 2-4 3-7 2-9-3-16-10-19-19-1-3 0-6 2-7z" fill="var(--gold)"/>
      </svg>
      <span class="phone-number">0477250618</span>
    </div>

    <div class="ornament" role="img" aria-label="Gold filigree scroll ornament above the name"></div>

    <h1 class="card-name">Lina Frost</h1>

    <ul class="services">
      <li class="service">
        <svg class="tick" viewBox="0 0 16 16" aria-hidden="true"><path d="M2 8l4 4 8-9" fill="none" stroke="var(--ink-light)" stroke-width="2.5"/></svg>
        Events
      </li>
      <li class="service">
        <svg class="tick" viewBox="0 0 16 16" aria-hidden="true"><path d="M2 8l4 4 8-9" fill="none" stroke="var(--ink-light)" stroke-width="2.5"/></svg>
        Entertainment.
      </li>
      <li class="service">
        <svg class="tick" viewBox="0 0 16 16" aria-hidden="true"><path d="M2 8l4 4 8-9" fill="none" stroke="var(--ink-light)" stroke-width="2.5"/></svg>
        Promotions
      </li>
    </ul>
  </section>
</main>
</body>
</html>
```